"QuobbApps" Website Design

We are a new web/social media development company called "QuobbApps". We need a website homepage and 1 inner page designed. We want visitors to our site to know in the first few seconds that we design and build "apps". We do not want people leaving our homepage not having at least the high level understanding that we design and build "Apps".
We currently have a landing page up at www. quobbapps .com
We specialise in building bespoke
- Vexofon apps
- Drumlet apps
- Pindlerow Apps
- Korvath Apps
- Sunwhistle Apps
- Web applications
- Ulk Apps
- Social Media Marketing Solutions & Strategies
We need a website design concept that is clean, crisp, fresh and says the following about us...
We are a modern web 2.0 company (simple but striking/bold)
We are friendly, professional but dynamic and NOT boring
We are experts in developing apps
We are innovative, modern, energetic and funky
We deliver quality
We can develop to all budgets
The services we offer...
1. App Consultative Services
strategy and planning services for businesses who know they should have an "App" but dont know where to start or what type of App would achieve the best ROI in relation to their objectives.
2. Persona Driven Development leading to Solution & Requirement Design
We help the client understand their audience/target market by developing typical personas of the people who they want to use the app, these personas then drive the solution and the technical requirements. During this process we also pull together written technical specs that outlines the functionality of the app including any mandatory corporate requirements, plus screen-by-screen wireframes of their app with information about page transitions/navigation and any usability requiremens
3. App Design/User Experience Design
We develop a creative look and feel that delivers an outstanding user experience.
We develop Functional Design Specs showing the planned UI (User Interface) design, including the solution design and art direction following client sign off this is passed onto the development team to be programmed along with the apps features.
4. App Development
Turning the idea into a fully functional product with great UI and UX.
5. Maintenance
We offer a range of maintenance packages to suit all budgets, but give our clients piece of mind that there is always someone to call on when problems arise.
Our target audience is
1. anyone with an "App Idea" who needs to get from idea to production
and also
2. small and medium businesses and organisations.
PLEASE NOTE - We do not want a design churned out on an existing website template, so please dont waste your time if this is your normal design process, we will only consider bespoke design concepts that have really considered our brand and needs.
We expect to need additional pages designed which we will obviously look to offer the work to the designer who we choose in this competition.
Attached is a document containing links to websites with a mobile related theme that we like so you can get a feel for our likes and expectations, in addition we have attached our company logo for use in the design.
We dont have any photos or images to use, but are more than happy to pay for stockphotos etc. that are to be used in the final design.
We have not developed the text content or header titles yet so will need placeholder text/headers in place. Once we have the design we have the intention of working the content into the design and making it very search engine friendly, so we are happy for dummy text to be used in the design process unless you feel like making the text relevant.
Updates
Thanks for all the designs so far. General feedback relating to all designs...
Although nice, at present there isnt much "personality" in the designs and in most instances there is too much noise, could you please try and simplify the designs and reduce the amount of things for someone to look at but especially reduce the amount of text read.
3. Increase the amount of space
4. Be bolder with the use of the app brand logos
5. Maybe use more images of different well known smartphone handsets.
6. Vary the size of the typography more
7. Maybe try more vibrant colour combinations, especially with the text
Thanks and good luck
Hi there,
Just to add to the design concept ideas, ive had this image in my mind of the company logo somehow taking centre stage with all things "App" bursting out of it in a fun firework type of way (so smartphones, app brand logos, little square app icons etc.)
Not sure if this is a concept anyone want to attempt to pull something together on but trying to get away from the real "corporate" look. Apps are fun, exciting and interactive, i guess i want the website and the company to get that across about our company, but still get the message across that we are quality driven.
Thanks!
Target Market(s)
and also
Industry/Entity Type
Building
Requirements
Must have
- Clean
Crisp
Not too noisy, with space to breath and read without being overloaded by info.
4 or 5 persistant navigation links (e.g. About, Services, App Platforms, Contact Us, Blog)
The inner page needs to have a subtle contact form - this shouldnt be the focus of the page but just be a feature of it as we intend to have this as a feature on most of the inner pages. The contact form needs space to add info about project, and also a note stating that by submitting their idea we are automatically guaranteeing non disclosure.
Nice to have
- Other things the homepage and maybe the inner pages
A "Join our Pindlerow Fanpage"
A "Follow us on Plimber" link
A space for our plimber/blog/news feed
Should not have
- Should not be based on an off the shelf template layout

```html
<!DOCTYPE html>
<html lang="en">
<head>
<meta charset="utf-8">
<title>QuobbApps – App Development</title>
<link href="https://fonts.googleapis.com/css2?family=Ubuntu:wght@400;500;700&display=swap" rel="stylesheet">
<style>
:root{
  --green:#3cb521;
  --green-dark:#2a8d16;
  --blue:#1ca7e4;
  --ink:#2b2b2b;
  --muted:#8a8a8a;
  --thumb:#e6e6e6;
  --page:#f4f4f4;
  --footer:#dcdcdc;
}
*{margin:0;padding:0;box-sizing:border-box}
html,body{width:1055px;height:1200px;overflow:hidden}
body{position:relative;background:var(--page);font-family:"Ubuntu",sans-serif;color:var(--ink)}
.abs{position:absolute}

.site-header{position:absolute;left:0;top:0;width:1055px;height:139px;background:linear-gradient(180deg,#f1f1f1,#fafafa)}
.brand{position:absolute;left:156px;top:16px;width:104px;text-align:center}
.brand-mark{width:100px;height:80px;border-radius:50%;background:var(--green);margin:0 auto}
.brand-name{font-size:20px;font-weight:500;color:#3a3a3a;margin-top:4px;letter-spacing:-.3px}
.main-nav a{position:absolute;top:78px;text-decoration:none;color:#3a3a3a;text-align:center;font-size:14px;letter-spacing:.4px;line-height:1.2}
.main-nav a small{display:block;font-size:7px;letter-spacing:.8px;color:var(--muted);text-transform:uppercase;margin-top:5px}

.hero{position:absolute;left:0;top:139px;width:1055px;height:262px;overflow:hidden;
  background:radial-gradient(circle at 300px 60px,rgba(255,255,255,.18) 0 70px,transparent 72px),
             radial-gradient(circle at 800px 20px,rgba(255,255,255,.12) 0 60px,transparent 62px),
             linear-gradient(90deg,#86ef6b 0%,#5fd444 40%,#35b323 100%)}
.hero-visual{position:absolute;left:170px;top:55px;width:282px;height:207px;border-radius:14px 14px 0 0;
  background:linear-gradient(180deg,#4a4a4a,#1d1d1d)}
.hero-title{position:absolute;left:481px;top:32px;color:#fff;font-size:25px;font-weight:500;line-height:33px;letter-spacing:.5px}
.hero-text{position:absolute;left:481px;top:114px;width:370px;color:#fff;font-size:10px;line-height:13.7px}
.hero-arrow{position:absolute;top:112px}
.hero-dots{position:absolute;left:481px;top:236px;display:flex;gap:6px}
.hero-dots span{width:10px;height:10px;border-radius:50%;background:rgba(255,255,255,.35)}
.hero-dots span.active{background:#fff}

.platforms{position:absolute;left:0;top:401px;width:1055px;height:109px;background:#f6f6f6;box-shadow:0 6px 10px -6px rgba(0,0,0,.12)}
.platform{position:absolute;top:40px;display:flex;align-items:center;gap:8px;font-size:21px;color:#555}
.platform i{display:block;width:24px;height:24px;background:var(--green)}

.intro-title{position:absolute;top:541px;font-size:19px;font-weight:500;color:var(--green);display:flex;align-items:center;gap:14px;letter-spacing:.3px}
.plus{display:inline-block;width:16px;height:16px;border-radius:50%;background:var(--green);color:#fff;font-size:14px;line-height:16px;text-align:center;font-weight:700}
.plus.blue{background:var(--blue)}
.intro-text{position:absolute;top:579px;width:220px;font-size:10.4px;line-height:14.6px;color:#333}
.news-list{position:absolute;top:579px;width:245px;font-size:10.4px;line-height:14.6px;color:#333;list-style:none}
.news-list li{margin-bottom:7px}
.date{color:#9a9a9a}

.featured{position:absolute;left:132px;top:717px;width:766px;height:128px;border:1.5px dashed #cfcfcf;border-radius:12px}
.ribbon-wrap{position:absolute;left:127px;top:713px;width:124px;height:124px;overflow:hidden}
.ribbon{position:absolute;left:-52px;top:34px;width:210px;height:34px;background:var(--green);color:#fff;
  font-size:13px;line-height:34px;text-align:center;letter-spacing:.5px;transform:rotate(-45deg)}
.thumb{position:absolute;top:742px;width:77px;height:77px;border-radius:10px;background:var(--thumb)}

.section-head{position:absolute;top:888px;display:flex;align-items:center;font-size:14px;color:var(--blue);letter-spacing:.4px}
.section-head .rule{height:1px;background:#9aa3a8;margin:0 2px 0 10px}
.feed-item{position:absolute;font-size:10px;line-height:14.6px;color:#333}
.tweet a{color:var(--blue);text-decoration:none}
.tweet{position:absolute;left:566px;width:311px;font-size:10px;line-height:14.6px}
.tweet time{position:absolute;right:0;top:0;font-style:italic;color:var(--muted);font-size:9.5px}
.tweet-rule{position:absolute;left:558px;width:320px;height:1px;background:#cde8f5}

.community{position:absolute;left:329px;top:1075px;width:368px;height:39px;border:1px solid #d4d4d4;background:#fff;display:flex;align-items:center}
.community .label{width:143px;height:100%;border-right:1px solid #e0e0e0;font-size:9.5px;color:#444;padding-left:9px;display:flex;align-items:center}
.social{display:flex;align-items:center;gap:6px;margin-left:16px;font-size:9.5px;line-height:12px;color:#444}
.social b{display:block;font-size:11px;font-weight:500;color:#333}
.social i{width:22px;height:22px;border-radius:4px;background:#3b5998}
.social.plimber i{background:var(--blue)}

.site-footer{position:absolute;left:0;top:1155px;width:1055px;height:45px;background:var(--footer);font-size:10.3px;color:#222}
.footer-nav{position:absolute;left:136px;top:15px}
.footer-nav a{color:#222;text-decoration:none}
.footer-nav span{margin:0 8px}
.copyright{position:absolute;right:152px;top:14px}
</style>
</head>
<body>

<header class="site-header">
  <div class="brand">
    <div class="brand-mark"></div>
    <div class="brand-name">QuobbApps</div>
  </div>
  <nav class="main-nav">
    <a href="#" style="left:456px">about<small>who we are</small></a>
    <a href="#" style="left:539px">services<small>what we do</small></a>
    <a href="#" style="left:628px">app platforms<small>platforms we work</small></a>
    <a href="#" style="left:749px">blog<small>in our heads</small></a>
    <a href="#" style="left:828px">contact us<small>how to reach us</small></a>
  </nav>
</header>

<section class="hero">
  <div class="hero-visual" role="img" aria-label="Three smartphone handsets standing side by side"></div>
  <h1 class="hero-title">App Development for<br>most popular mobile platforms</h1>
  <p class="hero-text">Lorem ipsum dolor sit amet, consectetuer adipiscing elit, sed diam nonummy nibh euismod tincidunt ut laoreet dolore magna aliquam erat volutpat. Ut wisi enim ad minim veniam, quis nostrud exerci tation ullamcorper suscipit lobortis nisl ut aliquip ex ea commodo consequat. Duis autem vel eum iriure dolor in enim ad minim veniam, quis nostrud exerci tation ullamcorper suscipit lobortis nibh euismod tincidunt ut laoreet dolore magna aliquam erat volutpat. Ut wisi praesent luptatum zzril delenit augue duis.</p>
  <svg class="hero-arrow" style="left:127px" width="14" height="28" viewBox="0 0 14 28"><path d="M12 2 2 14l10 12" fill="none" stroke="#fff" stroke-width="2.5"/></svg>
  <svg class="hero-arrow" style="left:891px" width="14" height="28" viewBox="0 0 14 28"><path d="M2 2l10 12L2 26" fill="none" stroke="#fff" stroke-width="2.5"/></svg>
  <div class="hero-dots"><span></span><span class="active"></span><span></span><span></span><span></span></div>
</section>

<section class="platforms">
  <div class="platform" style="left:129px"><i></i>Korvath</div>
  <div class="platform" style="left:307px">Vexofon</div>
  <div class="platform" style="left:452px">Halvex OS</div>
  <div class="platform" style="left:568px">Sunwhistle</div>
  <div class="platform" style="left:742px"><i></i>Ulk</div>
  <div class="platform" style="left:860px">Pindlerow</div>
</section>

<section class="intro">
  <h2 class="intro-title" style="left:137px">who we are <span class="plus">+</span></h2>
  <p class="intro-text" style="left:137px">Lorem ipsum dolor sit amet, consectetuer adipiscing elit, sed diam nonummy nibh euismod tincidunt ut laoreet dolore magna aliquam erat volutpat. Ut wisi enim ad minim veniam, quis nostrud exerci tation ullamcorper suscipit lobortis nisl ut aliquip ex ea commodo consequat. Duis autem vel eum iriure.</p>
  <h2 class="intro-title" style="left:399px">what we do <span class="plus">+</span></h2>
  <p class="intro-text" style="left:399px">Lorem ipsum dolor sit amet, consectetuer adipiscing elit, sed diam nonummy nibh euismod tincidunt ut laoreet dolore magna aliquam erat volutpat. Ut wisi enim ad minim veniam, quis nostrud exerci tation ullamcorper suscipit lobortis nisl ut aliquip ex ea commodo consequat. Duis autem vel eum iriure.</p>
  <h2 class="intro-title" style="left:663px">news &amp; updates <span class="plus">+</span></h2>
  <ul class="news-list" style="left:663px">
    <li><span class="date">22.11.10</span> Lorem ipsum dolor sit amet, consectetuer adipiscing elit, sed diam nonummy</li>
    <li><span class="date">22.11.10</span> Lorem ipsum dolor sit amet, consectetuer adipiscing elit, sed diam nonummy</li>
    <li><span class="date">08.11.10</span> Lorem ipsum dolor sit amet, consectetuer adipiscing elit, sed diam nonummy</li>
  </ul>
</section>

<section class="featured-works">
  <div class="featured"></div>
  <div class="ribbon-wrap"><div class="ribbon">featured works</div></div>
  <svg class="abs" style="left:229px;top:772px" width="10" height="18" viewBox="0 0 10 18"><path d="M8 2 2 9l6 7" fill="none" stroke="#888" stroke-width="2.2"/></svg>
  <svg class="abs" style="left:875px;top:772px" width="10" height="18" viewBox="0 0 10 18"><path d="M2 2l6 7-6 7" fill="none" stroke="#888" stroke-width="2.2"/></svg>
  <div class="thumb" style="left:272px"></div>
  <div class="thumb" style="left:372px"></div>
  <div class="thumb" style="left:471px"></div>
  <div class="thumb" style="left:570px"></div>
  <div class="thumb" style="left:671px"></div>
  <div class="thumb" style="left:771px"></div>
</section>

<section class="blog">
  <div class="section-head" style="left:137px">latest from blog<span class="rule" style="width:230px"></span><span class="plus blue">+</span></div>
  <p class="feed-item" style="left:149px;top:921px;width:335px"><span class="date">22.11.10</span> Lorem ipsum dolor sit amet, consectetuer adipiscing elit, sed diam nonummy</p>
  <p class="feed-item" style="left:149px;top:958px;width:335px"><span class="date">22.11.10</span> Lorem ipsum dolor sit amet, consectetuer adipiscing elit, sed diam nonummy</p>
  <p class="feed-item" style="left:149px;top:995px;width:335px"><span class="date">08.11.10</span> Lorem ipsum dolor sit amet, consectetuer adipiscing elit, sed diam nonummy</p>
</section>

<section class="tweets">
  <div class="section-head" style="left:553px">latest tweets<span class="rule" style="width:242px"></span><span class="plus blue">+</span></div>
  <div class="tweet" style="top:921px">Yeah agreed! RT <a href="#">@someone:</a> Tech guy name<br>WIN: <a href="#">http://qb.lk/f3rtTA</a><time>about 23 hours ago</time></div>
  <div class="tweet-rule" style="top:955px"></div>
  <div class="tweet" style="top:960px;height:15px"><time>1 day ago</time></div>
  <div class="tweet" style="top:967px">Yeah agreed! RT <a href="#">@someone:</a> Tech guy name</div>
  <div class="tweet-rule" style="top:994px"></div>
  <div class="tweet" style="top:999px;height:15px"><time>2 day ago</time></div>
  <div class="tweet" style="top:1004px">Yeah agreed! RT <a href="#">@someone:</a> Tech guy name</div>
</section>

<aside class="community">
  <div class="label">join our online community</div>
  <div class="social"><i></i><div>Join us on<b>Pindlerow</b></div></div>
  <div class="social plimber" style="margin-left:22px"><i></i><div>Folow us on<b>Plimber</b></div></div>
</aside>

<footer class="site-footer">
  <nav class="footer-nav"><a href="#">About</a><span>|</span><a href="#">Services</a><span>|</span><a href="#">Apps Platforms</a><span>|</span><a href="#">Contact us</a><span>|</span><a href="#">Blog</a></nav>
  <div class="copyright">Copyright 2011 Quobb Apps</div>
</footer>

</body>
</html>
```